KVORB Student Exchange needs a brochure design

I need a brochure design for KVORB Student Exchange based in Auckland, New Zealand. I am responsible for outbound exchanges where I recruit local students from around New Zealand between the ages of 15 and 18 who are interested in going on an exchange overseas. Students can select from 12 different countries including America, France, Italy, the Netherlands, Spain, Ireland, Germany, Brazil Japan, and Argentina and choose the programme length from 3 months to an academic year (although we offer shorter programmes for some countries). I would like to attract students who are keen to learn about other cultures and experience something completely different to home. I would like to see vibrant colours and images that coveys fun, youthfulness and adventure.
Updates

Hi,

I have added pics and content for your viewing. 

Thanks.

Tessa

Hi,

Could I request that the designs are done on a tri-fold brochure

Also, I would like to see vibrant colours. So far, I have seen colours matching the logo (which is ok)  but I want to try and move away from that and start something fresh. Please look at the booklet and fee sheet which I have uploaded for ideas. 

I am wondering whether there is too much writing to fit on a tri fold brochure...
If you are having problems fitting everything in, please let me know.

I think the testimonial section could use up 2 spaces on the brochure. 

Target Market(s)

I would like to target teenagers who are interested in other cultures and want to enhance their language learning

Industry/Entity Type

Learn

Font styles to use
Serif
Sans Serif
Decorative

```html
<!DOCTYPE html>
<html lang="en">
<head>
<meta charset="utf-8">
<title>KVORB Student Exchange – Tri-fold Brochure Inside Spread</title>
<link rel="stylesheet" href="https://fonts.googleapis.com/css2?family=Bebas+Neue&family=Open+Sans:wght@400;600&display=swap">
<style>
  :root {
    --page-bg: #ededed;
    --paper: #ffffff;
    --teal: #1f9a8a;
    --teal-dark: #167a6e;
    --purple: #6b4fa6;
    --ink: #111111;
    --body-text: #555555;
    --green-accent: #1f9a6a;
    --sky-top: #8fb3dc;
    --sky-bottom: #dfe9f4;
    --photo-warm: #c9a58c;
    --photo-cool: #8a9cc0;
  }
  * { margin: 0; padding: 0; box-sizing: border-box; }
  html, body { width: 1200px; height: 1200px; overflow: hidden; }
  body { background: var(--page-bg); font-family: "Open Sans", Arial, sans-serif; }

  .brochure {
    position: absolute; left: 90px; top: 230px;
    width: 1020px; height: 740px;
    display: flex; background: var(--paper);
    box-shadow: 0 10px 30px rgba(0,0,0,0.18);
  }
  .panel { position: relative; width: 340px; height: 100%; overflow: hidden; }
  .panel + .panel { border-left: 1px solid #e2e2e2; }

  .headline {
    font-family: "Bebas Neue", "Arial Narrow", sans-serif;
    font-weight: 400; letter-spacing: 0.5px; line-height: 1;
  }
  .body-copy { font-size: 12.5px; line-height: 1.45; color: var(--body-text); }

  /* Left panel */
  .panel-intro .shape-layer { position: absolute; inset: 0; }
  .panel-intro .intro-heading {
    position: absolute; top: 70px; left: 0; width: 100%;
    text-align: center; color: #fff; font-size: 30px;
  }
  .panel-intro .intro-copy {
    position: absolute; top: 112px; left: 26px; right: 26px;
    color: #fff; text-align: justify; font-size: 12.5px; line-height: 1.45;
  }

  /* Sky strip across middle & right */
  .sky-strip { position: absolute; top: 0; left: 0; right: 0; height: 110px; }
  .tagline {
    position: absolute; top: 32px; left: 20px;
    color: var(--purple); font-size: 30px; line-height: 0.95;
  }
  .people-photo { position: absolute; top: 0; right: 0; width: 150px; height: 110px; }

  .panel-content { padding: 0 30px; position: absolute; left: 0; right: 0; text-align: center; }
  .panel-content .headline { font-size: 30px; color: var(--ink); margin-bottom: 16px; }
  .panel-content p + p { margin-top: 16px; }
  .panel-middle .panel-content { top: 170px; }
  .panel-right .panel-content { top: 165px; }
  .accent-text { color: var(--green-accent); }

  .flags-strip { position: absolute; bottom: 0; left: 0; right: 0; height: 130px; }
</style>
</head>
<body>
  <main class="brochure">
    <!-- Left panel -->
    <section class="panel panel-intro">
      <svg class="shape-layer" width="340" height="740" viewBox="0 0 340 740">
        <defs>
          <linearGradient id="students-tones" x1="0" y1="0" x2="1" y2="1">
            <stop offset="0" stop-color="#c7a48a"/>
            <stop offset="0.5" stop-color="#9fb8a0"/>
            <stop offset="1" stop-color="#8a9cc0"/>
          </linearGradient>
        </defs>
        <polygon points="0,0 340,0 340,570 0,420" fill="var(--teal)"/>
        <polygon points="0,0 120,0 0,60" fill="#9fc0de" opacity="0.7"/>
        <polygon points="0,530 340,610 340,740 0,740" fill="url(#students-tones)" role="img" aria-label="Photo of a group of smiling teenage students"/>
      </svg>
      <h2 class="headline intro-heading">Lorem Ipsum Dolor</h2>
      <p class="intro-copy">consectetur adipiscing elit. Mauris feugiat ante a augue vestibulum, et ultrices massa congue. Vestibulum arcu mauris, interdum convallis placerat id, pretium vitae diam. Maecenas vel viverra elit, eu bibendum lorem. Pellentesque habitant morbi tristique senectus et netus et malesuada fames ac turpis egestas. Duis quis elementum urna. Sed ac diam aliquet, suscipit sapien eleifend, tempus augue. Etiam sagittis nulla nec imperdiet luctus, tortor libero commodo nibh, ut convallis purus arcu non odio. Donec a ipsum ac urna dapibus luctus. Proin dignissim sollicitudin semper. Quisque fermentum dapibus scelerisque.</p>
    </section>

    <!-- Middle panel -->
    <section class="panel panel-middle">
      <svg class="sky-strip" width="340" height="110" viewBox="0 0 340 110" role="img" aria-label="Blue sky with soft clouds">
        <defs>
          <linearGradient id="sky-mid" x1="0" y1="0" x2="0" y2="1">
            <stop offset="0" stop-color="var(--sky-top)"/>
            <stop offset="1" stop-color="var(--sky-bottom)"/>
          </linearGradient>
        </defs>
        <rect width="340" height="110" fill="url(#sky-mid)"/>
      </svg>
      <svg class="people-photo" width="150" height="110" viewBox="0 0 150 110" role="img" aria-label="Photo of four smiling young friends posing together">
        <defs>
          <linearGradient id="friends-tones" x1="0" y1="0" x2="1" y2="1">
            <stop offset="0" stop-color="#b88c6e"/>
            <stop offset="0.6" stop-color="#d9a7b8"/>
            <stop offset="1" stop-color="#7f8fb0"/>
          </linearGradient>
        </defs>
        <rect width="150" height="110" fill="url(#friends-tones)"/>
      </svg>
      <h1 class="headline tagline">It's time to make<br>new friends</h1>
      <div class="panel-content">
        <h2 class="headline">Curabitur Accumsan Quis</h2>
        <p class="body-copy">Aenean pulvinar nisi mi, ultrices pellentesque purus dictum eu. Vestibulum varius ante in nisi vestibulum, vel adipiscing tellus placerat. Nullam vehicula, orci sed ultrices suscipit, neque tortor egestas nunc, id ultrices mauris velit et mauris. Fusce nec scelerisque ante. Aenean tempor luctus tincidunt. Duis cursus interdum dignissim. Aenean sagittis urna volutpat quam varius vulputate.</p>
        <p class="body-copy">Aenean feugiat sit amet velit eu mattis. Etiam sit amet ligula ligula. Mauris quis ligula bibendum sapien aliquam gravida vitae id arcu. Aliquam tortor nibh, iaculis sit amet suscipit eu, vestibulum vitae metus. Pellentesque eget convallis elit. Nam sit amet dapibus nulla. In hac habitasse platea dictumst.</p>
      </div>
      <svg class="flags-strip" width="340" height="130" viewBox="0 0 340 130" role="img" aria-label="Photo of many national flags on poles against a blue sky">
        <defs>
          <linearGradient id="flags-left" x1="0" y1="0" x2="1" y2="1">
            <stop offset="0" stop-color="#7fa3d6"/>
            <stop offset="0.5" stop-color="#c65a5a"/>
            <stop offset="1" stop-color="#3f5fa8"/>
          </linearGradient>
        </defs>
        <rect width="340" height="130" fill="url(#flags-left)"/>
      </svg>
    </section>

    <!-- Right panel -->
    <section class="panel panel-right">
      <svg class="sky-strip" width="340" height="110" viewBox="0 0 340 110" role="img" aria-label="Blue sky with soft clouds">
        <defs>
          <linearGradient id="sky-right" x1="0" y1="0" x2="0" y2="1">
            <stop offset="0" stop-color="var(--sky-top)"/>
            <stop offset="1" stop-color="var(--sky-bottom)"/>
          </linearGradient>
        </defs>
        <rect width="340" height="110" fill="url(#sky-right)"/>
      </svg>
      <div class="panel-content">
        <h2 class="headline">Nin Faucibus.</h2>
        <p class="body-copy">Nullam lorem est, tincidunt vel tincidunt a, molestie a mauris. Curabitur accumsan quis magna vehicula dignissim. Pellentesque varius felis at nisl ultricies tempor at at nulla. Fusce eget massa quis leo laoreet elementum vitae eget dui. Cras tristique ultricies gravida. Duis tortor nisl, tristique ac orci ut, dictum pellentesque elit. Quisque sed blandit mi, vitae ornare mi. In hac habitasse platea dictumst. Etiam non tortor porttitor, lacinia neque vitae, feugiat diam. Praesent suscipit, ipsum non <span class="accent-text">condimentum mattis, mi diam convallis dui, sed porta felis neque volutpat quam.</span></p>
      </div>
      <svg class="flags-strip" width="340" height="130" viewBox="0 0 340 130" role="img" aria-label="Photo of many national flags on poles against a blue sky">
        <defs>
          <linearGradient id="flags-right" x1="0" y1="0" x2="1" y2="1">
            <stop offset="0" stop-color="#3f5fa8"/>
            <stop offset="0.5" stop-color="#d46a5a"/>
            <stop offset="1" stop-color="#8fb3dc"/>
          </linearGradient>
        </defs>
        <rect width="340" height="130" fill="url(#flags-right)"/>
      </svg>
    </section>
  </main>
</body>
</html>
```